Bricks in the Wall

We need graphics for a 5x7 or 6x9 post card, single sided for a small speech language pathology practice that serves pediatric patients primarily with children on the autism spectrum.

I want a brick wall, with words and phrases written into the bricks. (to follow)
A child standing on top of the wall with hands up in success.
A few incomplete autism puzzles on the ground.
A larger complete autism puzzle in the the child's hand.
The title is: Speech/Language Therapy
The Foundation for Communication Success
Words/phrases to go into the red bricks:
Receptive Language, Expressive Language, Pragmatics, Sensory, cognitive,
social language, autism, articulation, TeleTherapy, auditory processing, screening, evaluation, developmental delay, Goals, family involvement, environmental communication, ASD, Mirror Neurons.

Target Market(s)

Children with speech and language disorders.

Industry/Entity Type

Speech and Language Therapy

Font styles to use
Serif

Requirements
Must have
• Colors, primary and red bricks.
Nice to have
• I want the postcard to have a happy feel to it and a sense of success.
Should not have
• I don't want it cluttered.

```html
<!DOCTYPE html>
<html lang="en">
<head>
<meta charset="utf-8">
<title>Speech Language Therapy</title>
<link rel="stylesheet" href="https://fonts.googleapis.com/css2?family=Luckiest+Guy&family=Archivo+Black&family=Archivo:wght@700&display=swap">
<style>
  :root {
    --sky-light: #d8f4ff;
    --sky-mid: #5fc8f2;
    --sky-deep: #1583e6;
    --title-green: #1fc21f;
    --title-orange: #e8a20e;
    --title-red: #f0141c;
    --band-blue: #0a3ae8;
    --white: #ffffff;
    --cap-grey: #8d8f92;
    --cap-dark: #5e6063;
    --mortar: #7a3e22;
    --brick: #c9744d;
    --brick-light: #d98a62;
    --brick-text: #4e2211;
    --sand: #e8a35a;
    --sand-dark: #d48840;
    --brand-green: #1e7d22;
    --art-tone: #8fc4ee;
  }
  * { margin: 0; padding: 0; box-sizing: border-box; }
  html, body { width: 1200px; height: 857px; overflow: hidden; background: var(--white); }
  .postcard {
    position: relative; width: 1200px; height: 857px; overflow: hidden;
    background: radial-gradient(ellipse 55% 70% at 50% 38%, var(--sky-light) 0%, var(--sky-mid) 45%, var(--sky-deep) 100%);
  }
  .corner-art {
    position: absolute; left: 102px; top: 13px; width: 120px; height: 118px;
    border-radius: 6px;
    background: var(--art-tone);
    opacity: 0.55;
  }
  .title {
    position: absolute; left: 247px; top: 14px; width: 830px;
    font-family: "Luckiest Guy", "Archivo Black", sans-serif; font-size: 50px; line-height: 52px;
    letter-spacing: 1px; white-space: nowrap; text-align: center;
    text-shadow: 2px 2px 0 var(--white), -2px -2px 0 var(--white), 2px -2px 0 var(--white), -2px 2px 0 var(--white);
  }
  .title .w1 { color: var(--title-green); }
  .title .w2 { color: var(--title-orange); }
  .title .w3 { color: var(--title-red); }
  .tagline {
    position: absolute; left: 286px; top: 66px; width: 737px; height: 29px;
    background: linear-gradient(90deg, rgba(10,58,232,0) 0%, var(--band-blue) 12%, var(--band-blue) 88%, rgba(10,58,232,0) 100%);
    color: var(--white); font-family: "Archivo", sans-serif; font-weight: 700; font-size: 17px;
    line-height: 29px; text-align: center; letter-spacing: 0.3px;
  }
  .child-photo {
    position: absolute; left: 434px; top: 111px; width: 316px; height: 304px;
    border-radius: 40% 40% 12% 12%;
    background: linear-gradient(180deg, rgba(60,40,40,0.55) 0%, rgba(40,60,110,0.55) 55%, rgba(30,50,100,0.45) 100%);
  }
  .wall-cap {
    position: absolute; left: 0; top: 418px; width: 1200px; height: 29px;
    background: linear-gradient(180deg, var(--cap-grey) 0%, var(--cap-dark) 100%);
    border-top: 3px solid #a9abae;
  }
  .wall {
    position: absolute; left: 0; top: 447px; width: 1200px; height: 316px;
    background: var(--mortar);
  }
  .brick {
    position: absolute; display: flex; align-items: center; justify-content: center;
    background: linear-gradient(180deg, var(--brick-light) 0%, var(--brick) 60%, #b9653f 100%);
    box-shadow: inset 0 -2px 0 rgba(0,0,0,0.18), inset 0 2px 0 rgba(255,255,255,0.12);
    font-family: "Archivo Black", sans-serif; font-size: 22px; letter-spacing: 1px;
    color: var(--brick-text); white-space: nowrap; overflow: hidden;
    text-shadow: 1px 1px 0 rgba(255,200,170,0.45), -1px -1px 0 rgba(0,0,0,0.3);
  }
  .ground {
    position: absolute; left: 0; top: 763px; width: 1200px; height: 94px;
    background: linear-gradient(180deg, var(--sand) 0%, var(--sand-dark) 100%);
  }
  .brand {
    position: absolute; left: 26px; top: 792px;
    font-family: "Archivo Black", sans-serif; font-size: 17px; color: var(--brand-green);
  }
  .puzzle-pile {
    position: absolute; left: 977px; top: 766px; width: 126px; height: 85px;
    border-radius: 30%;
    background: linear-gradient(135deg, #f0a800 0%, #1aa01a 35%, #1c3fe0 60%, #e81010 100%);
  }
</style>
</head>
<body>
<main class="postcard">
  <div class="corner-art" role="img" aria-label="Colourful puzzle pieces illustration"></div>
  <h1 class="title"><span class="w1">SPEECH</span> <span class="w2">LANGUAGE</span> <span class="w3">THERAPY</span></h1>
  <p class="tagline">A FOUNDATION FOR SUCCESSFUL COMMUNICATION</p>
  <div class="child-photo" role="img" aria-label="Photo of a happy boy in a striped sweater jumping with arms and legs spread, with white clouds behind"></div>

  <div class="wall-cap"></div>
  <section class="wall" aria-label="Brick wall of therapy topics">
    <div class="brick" style="left:0;top:0;width:422px;height:47px">RECEPTIVE LANGUAGE</div>
    <div class="brick" style="left:427px;top:0;width:56px;height:47px"></div>
    <div class="brick" style="left:487px;top:0;width:413px;height:47px">EXPRESSIVE LANGUAGE</div>
    <div class="brick" style="left:906px;top:0;width:43px;height:47px"></div>
    <div class="brick" style="left:953px;top:0;width:247px;height:47px">PRAGMATICS</div>

    <div class="brick" style="left:0;top:51px;width:270px;height:47px">PRAGMATICS</div>
    <div class="brick" style="left:275px;top:51px;width:79px;height:47px"></div>
    <div class="brick" style="left:359px;top:51px;width:194px;height:47px">SENSORY</div>
    <div class="brick" style="left:559px;top:51px;width:95px;height:47px"></div>
    <div class="brick" style="left:660px;top:51px;width:289px;height:47px">COGNITIVE</div>
    <div class="brick" style="left:954px;top:51px;width:246px;height:47px">TELETHERAPY</div>

    <div class="brick" style="left:0;top:103px;width:41px;height:49px"></div>
    <div class="brick" style="left:46px;top:103px;width:239px;height:49px">ARTICULATION</div>
    <div class="brick" style="left:289px;top:103px;width:41px;height:49px"></div>
    <div class="brick" style="left:335px;top:103px;width:294px;height:49px">SOCIAL LANGUAGE</div>
    <div class="brick" style="left:634px;top:103px;width:37px;height:49px"></div>
    <div class="brick" style="left:676px;top:103px;width:359px;height:49px">AUDITORY PROCESSING</div>
    <div class="brick" style="left:1040px;top:103px;width:34px;height:49px"></div>
    <div class="brick" style="left:1079px;top:103px;width:111px;height:49px;font-size:20px;letter-spacing:0.5px">AUTISM</div>
    <div class="brick" style="left:1194px;top:103px;width:6px;height:49px"></div>

    <div class="brick" style="left:0;top:154px;width:85px;height:51px"></div>
    <div class="brick" style="left:89px;top:154px;width:182px;height:51px">SCREENING</div>
    <div class="brick" style="left:277px;top:154px;width:77px;height:51px"></div>
    <div class="brick" style="left:360px;top:154px;width:194px;height:51px">EVALUATION</div>
    <div class="brick" style="left:559px;top:154px;width:95px;height:51px"></div>
    <div class="brick" style="left:660px;top:154px;width:111px;height:51px">GOALS</div>
    <div class="brick" style="left:777px;top:154px;width:423px;height:51px">DEVELOPMENTAL DELAY</div>

    <div class="brick" style="left:0;top:209px;width:357px;height:50px">DEVELOPMENTAL DELAY</div>
    <div class="brick" style="left:361px;top:209px;width:63px;height:50px"></div>
    <div class="brick" style="left:429px;top:209px;width:85px;height:50px"></div>
    <div class="brick" style="left:519px;top:209px;width:270px;height:50px">MIRROR NEURONS</div>
    <div class="brick" style="left:794px;top:209px;width:86px;height:50px"></div>
    <div class="brick" style="left:885px;top:209px;width:189px;height:50px">PRAGMATICS</div>
    <div class="brick" style="left:1079px;top:209px;width:84px;height:50px"></div>
    <div class="brick" style="left:1167px;top:209px;width:33px;height:50px"></div>

    <div class="brick" style="left:0;top:263px;width:86px;height:50px"></div>
    <div class="brick" style="left:90px;top:263px;width:464px;height:50px">FAMILY INVOLVEMENT</div>
    <div class="brick" style="left:559px;top:263px;width:518px;height:50px">ENVIRONMENTAL COMMUNICATION</div>
    <div class="brick" style="left:1082px;top:263px;width:118px;height:50px"></div>
  </section>

  <div class="ground"></div>
  <p class="brand">Bright Steps</p>
  <div class="puzzle-pile" role="img" aria-label="Loose orange, green, blue and red puzzle pieces on the ground"></div>
</main>
</body>
</html>
```